professional business card

A Clean looking business card for a money transfer company. Our company is call Velorix= Transfer + Send = Transcend (next level)
to show professionalism as well as some effects to show digital tech.

1 side to have position, name and address
2 side to have company name and show that we provide money exchange and cross-border money transfer

Target Market(s)

Remittance companies and high net worth individuals

Industry/Entity Type

Finance

Contact Information for Business Card

Name, address, email, title, services- money exchange and cross-border remittance

Requirements
Nice to have
• Digital age feel

```html
<!DOCTYPE html>
<html lang="en">
<head>
<meta charset="utf-8">
<title>Velorix — Business Card</title>
<link href="https://fonts.googleapis.com/css2?family=Montserrat:wght@500;600;700&family=Open+Sans:wght@400;600&display=swap" rel="stylesheet">
<style>
  :root{
    --bg-top:#8ea7c4;
    --bg-bottom:#6d83aa;
    --card-dark:#2b3947;
    --card-dark-deep:#1f2b37;
    --card-light:#ffffff;
    --ink:#2a3644;
    --accent:#5fc8d9;
    --text-light:#eef3f7;
    --text-muted:#c9d3dc;
  }
  *{box-sizing:border-box;margin:0;padding:0}
  html,body{width:1200px;height:876px;overflow:hidden}
  body{
    background:linear-gradient(160deg,var(--bg-top),var(--bg-bottom));
    font-family:"Open Sans",Arial,sans-serif;
    position:relative;
  }
  .card{
    position:absolute;
    width:520px;height:297px;
    border-radius:4px;
    box-shadow:0 18px 40px rgba(20,35,60,.35);
    overflow:hidden;
  }
  /* Front: personal details */
  .card--front{
    left:50px;top:290px;
    background:linear-gradient(135deg,var(--card-dark) 0%,#3a4856 45%,var(--card-dark-deep) 100%);
    color:var(--text-light);
  }
  .holder{position:absolute;left:44px;top:34px}
  .holder__name{
    font-family:"Montserrat",sans-serif;font-weight:700;
    font-size:19px;letter-spacing:.5px;text-transform:uppercase;
  }
  .holder__role{font-size:15px;color:var(--accent);margin-top:2px}
  .brand{
    position:absolute;left:44px;top:108px;
    display:flex;align-items:center;gap:12px;
  }
  .brand__mark{width:14px;height:14px;background:var(--accent);border-radius:2px}
  .brand__name{
    font-family:"Montserrat",sans-serif;font-weight:700;
    font-size:44px;letter-spacing:2px;text-transform:uppercase;line-height:1;
  }
  .card--front .brand__name{color:var(--text-light)}
  .service{
    position:absolute;left:44px;top:168px;
    font-size:13.5px;color:var(--text-muted);
  }
  .contacts{
    position:absolute;left:44px;bottom:34px;
    display:flex;align-items:flex-start;gap:14px;
    font-size:12.5px;color:var(--text-light);
    white-space:nowrap;
  }
  .contact{display:flex;align-items:flex-start;gap:7px;line-height:1.4}
  .contact svg{flex:none;width:17px;height:17px;margin-top:1px}
  .divider{width:1px;align-self:stretch;background:rgba(255,255,255,.55)}

  /* Back: company & services */
  .card--back{
    left:630px;top:290px;
    background:var(--card-light);
    color:var(--ink);
  }
  .card--back .brand{left:60px;top:66px}
  .card--back .brand__name{color:var(--ink);font-size:50px}
  .offer{
    position:absolute;left:60px;top:136px;
    font-family:"Montserrat",sans-serif;font-weight:500;
    font-size:14.5px;line-height:1.35;letter-spacing:.6px;
    text-transform:uppercase;color:var(--accent);
  }
  .website{
    position:absolute;left:60px;bottom:40px;
    font-size:15px;letter-spacing:11px;color:var(--ink);
  }
</style>
</head>
<body>

<section class="card card--front" aria-label="Business card front">
  <div class="holder">
    <p class="holder__name">Dana Morrow</p>
    <p class="holder__role">Director</p>
  </div>
  <div class="brand">
    <span class="brand__mark"></span>
    <span class="brand__name">Velorix</span>
  </div>
  <p class="service">Money exchange and cross-border remittance</p>
  <div class="contacts">
    <div class="contact">
      <svg viewBox="0 0 18 18" aria-hidden="true"><circle cx="9" cy="9" r="9" fill="#5fc8d9"/><rect x="6" y="4" width="6" height="10" rx="1.2" fill="#2b3947"/><rect x="7" y="5.3" width="4" height="6" fill="#5fc8d9"/></svg>
      <span>+000 55501 2468</span>
    </div>
    <span class="divider"></span>
    <div class="contact">
      <svg viewBox="0 0 18 18" aria-hidden="true"><circle cx="9" cy="9" r="9" fill="#5fc8d9"/><path d="M9 4a3.2 3.2 0 0 0-3.2 3.2C5.8 9.6 9 14 9 14s3.2-4.4 3.2-6.8A3.2 3.2 0 0 0 9 4z" fill="#2b3947"/><circle cx="9" cy="7.2" r="1.2" fill="#5fc8d9"/></svg>
      <span>48 Harbour Lane<br>Singapore, 4417</span>
    </div>
    <span class="divider"></span>
    <div class="contact">
      <svg viewBox="0 0 18 18" aria-hidden="true"><circle cx="9" cy="9" r="9" fill="#5fc8d9"/><rect x="4.5" y="6" width="9" height="6.5" rx="1" fill="#2b3947"/><path d="M4.8 6.4 9 9.6l4.2-3.2" fill="none" stroke="#5fc8d9" stroke-width="1"/></svg>
      <span>dana@velorix.com</span>
    </div>
  </div>
</section>

<section class="card card--back" aria-label="Business card back">
  <div class="brand">
    <span class="brand__mark"></span>
    <span class="brand__name">Velorix</span>
  </div>
  <p class="offer">We provide money exchange<br>and cross-border money transfer</p>
  <p class="website">www.velorix.com</p>
</section>

</body>
</html>
```